Design for three pages of a 12-page 4-color 8.5 x 11 magazine-type booklet

We will be taking the information from a webpage at glowmerestudies.org and putting it into a 12-page 4-color 8.5 x 11 magazine-type booklet that will look like an upscale company report. I need to have a design in Photoshop for the cover and two inside pages that I can use as the template for the pages. I likely will also need help putting it together once I start putting the contents into the pages. I may just decide on the content and have the designer create the booklet as an additional freelance contract. First, I need a design for (1) the front cover, (2) one information page taken from information on http://www.glowmerestudies.org/kvon-project-management-staff/, and (3) one of the pages that has a researcher from this page on it: http://www.glowmerestudies.org/teaching-people-how-to-have/. That's designs for three pages. The designs have to be very professional looking and businesslike. We will be using the booklet to pitch to foundations and philanthropists. The work on the publication itself would be additional freelance work on an hourly basis.

Serif

• Professional look

```html
<!DOCTYPE html>
<html lang="en">
<head>
<meta charset="utf-8">
<title>Glowmere Studies – Booklet Cover</title>
<link rel="stylesheet" href="https://fonts.googleapis.com/css2?family=Saira:wght@400;500;700;800&family=Open+Sans:wght@400;600&display=swap">
<style>
  :root {
    --backdrop: #3f4b51;
    --paper: #edf1f4;
    --paper-shade: #dfe6eb;
    --indigo: #2d2a80;
    --indigo-soft: #3a3596;
    --cyan: #3bb6ec;
    --grey-text: #5b6168;
    --sky-top: #5f8fcf;
    --sky-bottom: #c9d9ea;
    --glass: #2f4f8f;
  }
  * { box-sizing: border-box; margin: 0; padding: 0; }
  html, body { width: 1200px; height: 840px; overflow: hidden; }
  body { background: var(--backdrop); font-family: "Open Sans", sans-serif; }

  .cover {
    position: absolute; left: 290px; top: 20px;
    width: 620px; height: 800px;
    background: var(--paper);
    box-shadow: 0 10px 30px rgba(0,0,0,.35);
    overflow: hidden;
  }
  .cover-shapes { position: absolute; inset: 0; }

  .brand {
    position: absolute; right: 48px; top: 150px;
    font-family: "Saira", sans-serif; font-weight: 800;
    font-size: 78px; letter-spacing: 4px; line-height: 1;
    color: var(--indigo);
  }

  .identity {
    position: absolute; left: 300px; top: 330px; width: 300px;
    color: #fff; font-family: "Saira", sans-serif;
  }
  .identity-name { font-weight: 800; font-size: 30px; letter-spacing: 3px; line-height: 1.1; }
  .identity-sub { font-weight: 500; font-size: 22px; line-height: 1.2; margin-top: 4px; }

  .mission {
    position: absolute; left: 300px; top: 462px; width: 290px; color: #fff;
  }
  .mission-title {
    font-family: "Saira", sans-serif; font-weight: 500;
    font-size: 21px; color: var(--cyan); margin-bottom: 6px;
  }
  .mission-text { font-size: 12px; line-height: 1.45; }

  .tagline {
    position: absolute; left: 250px; top: 640px; width: 250px;
    text-align: center;
  }
  .tagline-head {
    font-family: "Saira", sans-serif; font-weight: 700;
    font-size: 21px; line-height: 1.1; color: var(--indigo); letter-spacing: 1px;
  }
  .tagline-rule { border: 0; border-top: 1px solid var(--grey-text); margin: 6px 0 4px; }
  .tagline-sub { font-family: "Saira", sans-serif; font-size: 19px; color: var(--grey-text); }
  .tagline-web { font-size: 12px; font-weight: 600; color: var(--indigo); margin-top: 10px; }
</style>
</head>
<body>
  <main class="cover">
    <svg class="cover-shapes" width="620" height="800" viewBox="0 0 620 800">
      <defs>
        <linearGradient id="skyline" x1="0" y1="0" x2="1" y2="1">
          <stop offset="0" stop-color="var(--sky-top)"/>
          <stop offset=".55" stop-color="var(--sky-bottom)"/>
          <stop offset="1" stop-color="var(--glass)"/>
        </linearGradient>
        <linearGradient id="band-lower" x1="0" y1="0" x2="1" y2="0">
          <stop offset="0" stop-color="var(--indigo-soft)"/>
          <stop offset="1" stop-color="var(--indigo)"/>
        </linearGradient>
      </defs>
      <g class="facets" fill="var(--paper-shade)" opacity=".8">
        <polygon points="400,800 520,560 620,800"/>
        <polygon points="520,800 600,620 620,680 620,800"/>
        <polygon points="0,560 120,800 0,800"/>
      </g>
      <polygon class="hero-photo" role="img" aria-label="Photograph of glass skyscrapers rising into a blue sky with white clouds"
               points="0,0 340,0 290,300 300,560 0,560" fill="url(#skyline)"/>
      <polygon class="accent-triangle" points="40,660 110,505 250,560" fill="var(--indigo)"/>
      <polygon class="name-band" points="280,300 620,300 620,440 300,440" fill="var(--indigo)"/>
      <polygon class="mission-band" points="300,440 620,440 620,600 290,600" fill="url(#band-lower)"/>
    </svg>

    <div class="brand">KVON</div>

    <div class="identity">
      <div class="identity-name">GLOWMERE</div>
      <div class="identity-sub">Studies and education<br>Institute. Inc.</div>
    </div>

    <div class="mission">
      <div class="mission-title">Bridging Heaven and Earth</div>
      <p class="mission-text">When al people realize we are eternal beungs, humankind will live together in love, peace, and joy.</p>
    </div>

    <div class="tagline">
      <div class="tagline-head">GLOWMERE<br>COMMUNICATION</div>
      <hr class="tagline-rule">
      <div class="tagline-sub">Transforms lives.</div>
      <div class="tagline-web">www.glowmerestudies.org</div>
    </div>
  </main>
</body>
</html>
```